New Business card with our new logo

NEW BUSINESS CARDS wth our new logo

Want a sophisticated look. Probably in deep purple ink. (but we are open)
Would like something that looks expensive. Do not want a cutsie food look.
Not sure what more information I can offer. If you have any please contact me.

NAME - Ruth Delacroix Hale, Owner
415-273 0918
ruth@velvetplatterco.example
velvetplatterco.example

Target Market(s)

not sure what your are asking?

Industry/Entity Type

Business

Contact Information for Business Card

Logo + informaiton
Want a sophisticated look if possible. The cards are for women

Font styles to use
Serif

Colors
886aae

Requirements
Must have
• Ruth Delacroix Hale, Owner
• 415-273 0918
• ruth@velvetplatterco.example
• velvetplatterco.example
Nice to have
• suprise me
Should not have
• No cute food images, chef hat, knives, forks, etc.

```html
<!DOCTYPE html>
<html lang="en">
<head>
<meta charset="utf-8">
<title>Velvet Platter – Business Card</title>
<link href="https://fonts.googleapis.com/css2?family=Montserrat:wght@300;400;600;700&display=swap" rel="stylesheet">
<style>
  :root {
    --plum: #5f4577;
    --plum-text: #5a3e78;
    --lavender: #886aae;
    --leaf: #8cc152;
    --paper: #ffffff;
    --stage: #ece8e2;
  }
  * { box-sizing: border-box; margin: 0; padding: 0; }
  html, body {
    width: 1200px; height: 800px; overflow: hidden;
    background: var(--stage);
    font-family: "Montserrat", sans-serif;
  }
  .sheet {
    width: 1200px; height: 800px;
    display: flex; align-items: center; justify-content: center; gap: 40px;
  }
  .card {
    width: 525px; height: 300px;
    border-radius: 16px;
    position: relative;
    box-shadow: 0 6px 18px rgba(60, 40, 80, 0.18);
    overflow: hidden;
  }
  .card--front { background: var(--plum); }
  .card--back { background: var(--paper); }

  .brand { position: absolute; display: flex; flex-direction: column; }
  .brand__name { font-weight: 600; letter-spacing: 1px; white-space: nowrap; line-height: 1.1; }
  .brand__tagline {
    font-size: 9px; font-weight: 600; letter-spacing: 1px;
    color: var(--leaf); white-space: nowrap; margin-top: 6px;
  }

  .card--front .brand { left: 0; right: 0; top: 118px; align-items: center; }
  .card--front .brand__name { color: var(--paper); font-size: 34px; }

  .card--back .brand { right: 34px; top: 50px; align-items: flex-end; }
  .card--back .brand__name { color: var(--plum-text); font-size: 24px; }

  .person {
    position: absolute; left: 34px; top: 150px;
    padding-left: 12px; border-left: 6px solid var(--lavender);
  }
  .person__name { font-size: 20px; color: var(--lavender); font-weight: 300; }
  .person__first { font-weight: 700; color: var(--plum-text); }
  .person__role { font-size: 13px; color: var(--leaf); font-weight: 600; margin-top: 2px; }

  .contacts {
    position: absolute; left: 40px; bottom: 26px;
    list-style: none; display: flex; flex-direction: column; gap: 7px;
  }
  .contacts__item {
    display: flex; align-items: center; gap: 10px;
    font-size: 13px; font-weight: 600; color: var(--plum-text);
  }
  .contacts__icon { width: 14px; height: 14px; flex: none; }
</style>
</head>
<body>
<main class="sheet">
  <section class="card card--front" aria-label="Card front">
    <div class="brand">
      <span class="brand__name">Velvet Platter</span>
      <span class="brand__tagline">FINE MEALS, THOUGHTFULLY MADE</span>
    </div>
  </section>

  <section class="card card--back" aria-label="Card back">
    <div class="brand">
      <span class="brand__name">Velvet Platter</span>
      <span class="brand__tagline">FINE MEALS, THOUGHTFULLY MADE</span>
    </div>

    <div class="person">
      <p class="person__name"><span class="person__first">Ruth</span> Delacroix Hale</p>
      <p class="person__role">Owner</p>
    </div>

    <ul class="contacts">
      <li class="contacts__item">
        <svg class="contacts__icon" viewBox="0 0 14 14" aria-hidden="true">
          <path d="M3 1.5h2.2l1 3-1.4 1.1a7 7 0 0 0 3.6 3.6L9.5 7.8l3 1v2.2c0 .8-.7 1.5-1.5 1.5A10.5 10.5 0 0 1 1.5 3c0-.8.7-1.5 1.5-1.5z" fill="#8cc152"/>
        </svg>
        415-273 0918
      </li>
      <li class="contacts__item">
        <svg class="contacts__icon" viewBox="0 0 14 14" aria-hidden="true">
          <rect x="1" y="3" width="12" height="8" rx="1" fill="#8cc152"/>
          <path d="M1.5 3.5 7 8l5.5-4.5" fill="none" stroke="#fff" stroke-width="1.2"/>
        </svg>
        ruth@velvetplatterco.example
      </li>
      <li class="contacts__item">
        <svg class="contacts__icon" viewBox="0 0 14 14" aria-hidden="true">
          <circle cx="7" cy="7" r="6" fill="none" stroke="#8cc152" stroke-width="1.4"/>
          <ellipse cx="7" cy="7" rx="2.5" ry="6" fill="none" stroke="#8cc152" stroke-width="1.1"/>
          <path d="M1 7h12" stroke="#8cc152" stroke-width="1.1"/>
        </svg>
        velvetplatterco.example
      </li>
    </ul>
  </section>
</main>
</body>
</html>
```